Business letterhead and powerpoint template

Hi, I have recently started using a new logo (found through MarkVesta) and would now like to use that logo for letterheads and powerpoint.

Attached is the logo and one version of a brochure I have recently used.

Business

```html
<!DOCTYPE html>
<html lang="en">
<head>
<meta charset="utf-8">
<title>Halden Capital – Letterhead and Slide Templates</title>
<link rel="stylesheet" href="https://fonts.googleapis.com/css2?family=Exo+2:wght@300;400&display=swap">
<style>
  :root {
    --stage: #000000;
    --brand: #ef4a24;
    --brand-soft: #f26a45;
    --paper: #ffffff;
    --rule-grey: #9a9a9a;
    --glow: rgba(255, 70, 30, 0.85);
    --ink-muted: #555555;
  }
  * { box-sizing: border-box; margin: 0; padding: 0; }
  html, body {
    width: 1200px; height: 877px; overflow: hidden;
    background: var(--stage);
    font-family: "Exo 2", Arial, sans-serif;
    font-weight: 300;
  }
  .canvas { position: relative; width: 1200px; height: 877px; }
  .sheet {
    position: absolute; overflow: hidden;
    box-shadow: 0 0 9px 2px var(--glow);
  }
  .slide { background: linear-gradient(135deg, var(--brand) 0%, var(--brand-soft) 55%, var(--brand) 100%); }
  .slide-surface { position: absolute; inset: 0; }
  .footer-curve { position: absolute; left: 0; bottom: 0; width: 100%; height: 100%; }
  .brand-name {
    position: absolute; color: var(--paper); font-weight: 300;
    letter-spacing: 1px; white-space: nowrap; line-height: 1;
  }
  .web-link {
    position: absolute; display: flex; align-items: center; gap: 4px;
    font-size: 7.5px; color: var(--ink-muted); white-space: nowrap;
  }
  .web-link .dot { width: 7px; height: 7px; border-radius: 50%; background: var(--brand); }

  /* Letterhead */
  .letterhead { left: 277px; top: 27px; width: 274px; height: 386px; background: var(--paper); }
  .letterhead-band { position: absolute; left: 0; top: 0; width: 100%; height: 39px; background: var(--brand); }
  .letterhead-band::after {
    content: ""; position: absolute; left: 0; right: 0; top: 7px; height: 1px; background: rgba(255,255,255,.7);
  }
  .letterhead .brand-name { left: 15px; top: 21px; font-size: 11px; }
  .letterhead-contact {
    position: absolute; left: 186px; top: 5px; list-style: none;
    font-size: 4px; color: var(--paper); line-height: 1.45;
  }
  .letterhead-contact li { display: flex; gap: 3px; align-items: flex-start; }
  .letterhead-contact .bullet { width: 4px; height: 4px; border-radius: 50%; background: var(--paper); margin-top: 1px; flex: none; }

  /* Title slide */
  .title-slide { left: 614px; top: 27px; width: 533px; height: 398px; }
  .title-slide .brand-name { right: 34px; top: 53px; font-size: 26px; }
  .title-slide .brand-rule { position: absolute; left: 302px; right: 0; top: 85px; height: 1px; background: var(--paper); }
  .contact-block {
    position: absolute; left: 0; right: 0; top: 358px; text-align: center;
    font-size: 7px; color: var(--ink-muted); line-height: 10px;
  }
  .contact-block .pin { display: inline-block; width: 6px; height: 8px; vertical-align: -1px; }
  .contact-block .dot { display: inline-block; width: 6px; height: 6px; border-radius: 50%; background: var(--brand); vertical-align: -1px; margin: 0 2px; }

  /* Content slide */
  .content-slide { left: 33px; top: 451px; width: 534px; height: 400px; }
  .content-heading { position: absolute; left: 21px; top: 21px; font-size: 16px; color: var(--paper); font-weight: 300; }
  .content-slide .brand-rule { position: absolute; left: 0; right: 16px; top: 43px; height: 1px; background: rgba(255,255,255,.8); }
  .content-slide .brand-name { right: 17px; top: 24px; font-size: 15px; }
  .content-body { position: absolute; left: 21px; top: 58px; width: 400px; color: var(--paper); }
  .content-body h3 { font-size: 11px; font-weight: 300; margin-bottom: 8px; }
  .content-body p { font-size: 9.4px; line-height: 12.6px; margin-bottom: 12.4px; }
  .content-slide .web-link { right: 32px; bottom: 15px; }

  /* Closing slide */
  .closing-slide { left: 614px; top: 451px; width: 533px; height: 400px; }
  .closing-title { position: absolute; left: 410px; top: 31px; font-size: 20px; color: var(--paper); font-weight: 300; }
  .closing-slide .title-rule { position: absolute; left: 410px; right: 0; top: 53px; height: 1px; background: var(--paper); }
  .closing-slide .brand-name { left: 216px; top: 314px; font-size: 22px; }
  .closing-slide .brand-rule { position: absolute; left: 216px; width: 142px; top: 344px; height: 1px; background: var(--paper); }
  .closing-slide .web-link { right: 32px; bottom: 15px; }
</style>
</head>
<body>
<main class="canvas">

  <section class="sheet letterhead" aria-label="Letterhead">
    <div class="letterhead-band"></div>
    <span class="brand-name">HALDEN CAPITAL</span>
    <ul class="letterhead-contact">
      <li><span class="bullet"></span><span>Level 8 Suite 14, 52 Harbour Lane<br>Eastbrook 3100 NSW, Australia</span></li>
      <li><span class="bullet"></span><span>+61 (0)2 5550 1234</span></li>
      <li><span class="bullet"></span><span>+61 (0)2 5550 5678</span></li>
      <li><span class="bullet"></span><span>www.haldencapital.com.au</span></li>
    </ul>
    <svg class="footer-curve" viewBox="0 0 274 386" preserveAspectRatio="none" aria-hidden="true">
      <path d="M0,376 Q140,374 274,362 L274,386 L0,386 Z" fill="var(--rule-grey)"/>
      <path d="M0,376 Q140,374 274,362" fill="none" stroke="var(--brand)" stroke-width="2"/>
    </svg>
  </section>

  <section class="sheet slide title-slide" aria-label="Title slide">
    <svg class="footer-curve" viewBox="0 0 533 398" preserveAspectRatio="none" aria-hidden="true">
      <path d="M0,342 Q280,350 533,312 L533,398 L0,398 Z" fill="var(--rule-grey)"/>
      <path d="M0,345 Q280,353 533,316 L533,398 L0,398 Z" fill="var(--paper)"/>
    </svg>
    <span class="brand-name">HALDEN CAPITAL</span>
    <div class="brand-rule"></div>
    <div class="contact-block">
      <div><svg class="pin" viewBox="0 0 6 8"><path d="M3,0 A3,3 0 0 1 6,3 C6,5 3,8 3,8 C3,8 0,5 0,3 A3,3 0 0 1 3,0 Z" fill="var(--brand)"/><circle cx="3" cy="3" r="1.1" fill="#fff"/></svg> Level 8 Suite 14, 52 Harbour Lane, Eastbrook 3100 NSW, Australia</div>
      <div><span class="dot"></span>+61 (0)2 5550 1234 <span class="dot"></span>+61 (0)2 5550 5678</div>
      <div><span class="dot"></span>www.haldencapital.com.au</div>
    </div>
  </section>

  <section class="sheet slide content-slide" aria-label="Content slide">
    <svg class="footer-curve" viewBox="0 0 534 400" preserveAspectRatio="none" aria-hidden="true">
      <path d="M0,371 Q280,380 534,346 L534,400 L0,400 Z" fill="var(--rule-grey)"/>
      <path d="M0,374 Q280,383 534,350 L534,400 L0,400 Z" fill="var(--paper)"/>
    </svg>
    <h2 class="content-heading">Heading Here</h2>
    <div class="brand-rule"></div>
    <span class="brand-name">HALDEN CAPITAL</span>
    <div class="content-body">
      <h3>Sub Head</h3>
      <p>Dummy Text Dummy Text Dummy Text Dummy Text Dummy Text Dummy Text Dummy Text Dummy Text Dummy Text Dummy Text Dummy Text Dummy Text Dummy Text Dummy Text Dummy Text Dummy Text Dummy Text Dummy Text Dummy Text Dummy Text Dummy Text Dummy Text Dummy Text Dummy Text Dummy Text Dummy Text Dummy Text Dummy Text Dummy Text Dummy Text Dummy Text Dummy Text</p>
      <p>Dummy Text Dummy Text Dummy Text Dummy Text Dummy Text Dummy Text Dummy Text Dummy Text Dummy Text Dummy Text Dummy Text Dummy Text Dummy Text Dummy Text Dummy Text Dummy Text Dummy Text Dummy Text Dummy Text Dummy Text Dummy Text Dummy Text Dummy Text Dummy Text Dummy Text Dummy Text Dummy Text Dummy Text Dummy Text Dummy Text Dummy Text Dummy Text</p>
      <p>Dummy Text Dummy Text Dummy Text Dummy Text Dummy Text Dummy Text Dummy Text Dummy Text Dummy Text Dummy Text Dummy Text Dummy Text Dummy Text Dummy Text Dummy Text Dummy Text Dummy Text Dummy Text Dummy Text Dummy Text Dummy Text Dummy Text Dummy Text Dummy Text Dummy Text Dummy Text Dummy Text Dummy Text Dummy Text Dummy Text Dummy Text Dummy Text</p>
      <p>Dummy Text Dummy Text Dummy Text Dummy Text Dummy Text Dummy Text Dummy Text Dummy Text Dummy Text Dummy Text Dummy Text Dummy Text Dummy Text Dummy Text Dummy Text Dummy Text</p>
    </div>
    <div class="web-link"><span class="dot"></span>www.haldencapital.com.au</div>
  </section>

  <section class="sheet slide closing-slide" aria-label="Closing slide">
    <svg class="footer-curve" viewBox="0 0 533 400" preserveAspectRatio="none" aria-hidden="true">
      <path d="M0,371 Q280,380 533,344 L533,400 L0,400 Z" fill="var(--rule-grey)"/>
      <path d="M0,374 Q280,383 533,348 L533,400 L0,400 Z" fill="var(--paper)"/>
    </svg>
    <h2 class="closing-title">Thank You</h2>
    <div class="title-rule"></div>
    <span class="brand-name">HALDEN CAPITAL</span>
    <div class="brand-rule"></div>
    <div class="web-link"><span class="dot"></span>www.haldencapital.com.au</div>
  </section>

</main>
</body>
</html>
```